Brightfernrx website

We are a weight loss clinic and we need a website built. please look at these websites for content and style. Just need like 5 pages see samples. AI files of logo are not avail yet so use sample for place set

https://glowshiftstudio.com/
ortanvital.com
https://pinecrestclinicalbodybalance.com/
https://yourslimmingnook.com/
https://qrvskinstudio.com/treatments/weight-loss-injections/

Target Market(s)

Women

Industry/Entity Type

weight loss

Coding

Coded - Design and coding required

Number of Pages Required

5+ page

Requirements
Nice to have
• please make look like a medspa website

```html
<!DOCTYPE html>
<html lang="en">
<head>
<meta charset="utf-8">
<title>Brightfernrx – Website Header Concepts</title>
<link href="https://fonts.googleapis.com/css2?family=Cinzel:wght@400&family=Open+Sans:wght@400;600&family=Arimo:wght@400&display=swap" rel="stylesheet">
<style>
  :root{
    --board:#ececec;
    --deep-teal:#0a4450;
    --teal:#0b8a78;
    --topbar:#0a8670;
    --fern:#8bbd4e;
    --sky:#29a8e0;
    --ocean:#2e86b0;
    --mist:#a9b8bf;
    --ink:#000;
    --nav:#2a7aa0;
    --white:#fff;
    --caption:#222;
  }
  *{margin:0;padding:0;box-sizing:border-box}
  html,body{width:1200px;height:297px;overflow:hidden;background:var(--board)}
  body{position:relative;font-family:"Open Sans",sans-serif}

  .screen{position:absolute;top:17.7px;width:273px;height:177.5px;background:var(--white);box-shadow:0 0 0 .4px #d4d4d4}
  .screen--home{left:28px}
  .screen--about{left:318px}
  .screen--treatments{left:608px}
  .screen--services{left:898px}

  .topbar{height:10.3px;background:var(--topbar);color:var(--white);font-size:3.6px;position:relative}
  .topbar span{position:absolute;top:3.3px;white-space:nowrap}
  .topbar .call{left:14px}
  .topbar .email{left:62px}
  .topbar .address{left:129px}

  .site-header{height:29px;position:relative;background:var(--white)}
  .brand{position:absolute;left:5px;top:9px;display:flex;align-items:center;gap:2px;font-family:"Cinzel",serif;font-size:8px;color:var(--teal)}
  .brand-dot{width:7px;height:7px;border-radius:50%;background:var(--fern)}
  .nav a{position:absolute;top:13px;font-size:3.7px;color:var(--nav);text-decoration:none;white-space:nowrap}
  .book{position:absolute;left:220px;top:9.8px;width:47px;height:10.3px;border-radius:5.2px;background:var(--ocean);color:var(--white);font-size:3.8px;font-weight:600;display:flex;align-items:center;justify-content:center}

  .hero{position:absolute;left:0;top:39.3px;width:273px;height:138.2px;overflow:hidden}
  .hero--leaf{background:linear-gradient(110deg,#1f6b52 0%,#2f8a6a 35%,#b47a55 55%,#2c7a5c 75%,#0f3a30 100%)}
  .hero--field{background:linear-gradient(180deg,#1b3a34 0%,#2f5a3c 35%,#3f7a3a 60%,#1f4a26 100%)}
  .hero--foliage{background:linear-gradient(100deg,#2e4a2a 0%,#4f6e40 40%,#b8a68c 58%,#6b805a 80%,#8c9a78 100%)}
  .hero--mist{background:linear-gradient(120deg,#8fa3b0 0%,#6a7f8e 45%,#4b5c6a 65%,#9aabb5 100%)}
  .hero-copy{position:absolute;left:9.3px;bottom:12px;color:var(--white);font-family:"Cinzel",serif}
  .hero-intro{font-size:4.5px;line-height:7px;letter-spacing:.1px}
  .hero-title{font-size:9.3px;margin-top:5.5px;white-space:nowrap}

  .caption{position:absolute;top:201px;text-align:right;width:273px;font-family:"Arimo",sans-serif;color:var(--caption);white-space:nowrap}
  .caption strong{font-weight:400;font-size:5.6px;letter-spacing:2px}
  .caption small{font-size:3.5px;letter-spacing:1.2px}

  .palette-title{position:absolute;left:28px;top:243px;font-family:"Arimo",sans-serif;font-size:6.6px;letter-spacing:2.4px;color:var(--caption)}
  .swatches{position:absolute;left:28px;top:261.8px;display:flex;gap:9.2px;list-style:none}
  .swatches li{width:27px;height:25.6px}

  .draft-note{position:absolute;left:671px;top:244px;width:529px;height:43px;background:var(--ink);color:var(--white);font-family:"Arimo",sans-serif;padding:2.5px 4px;font-size:5.2px;line-height:5.85px;white-space:nowrap}
  .draft-note .label{font-size:6.6px}
  .draft-note .label small{font-size:4px}
</style>
</head>
<body>

<section class="screen screen--home">
  <div class="topbar"><span class="call">Call: 000 000 0000</span><span class="email">Email: contact@brightfernrx.com</span><span class="address">Address: Brightfern RX Headquarters Address information details t be added</span></div>
  <header class="site-header">
    <div class="brand"><span class="brand-dot"></span>Brightfernrx</div>
    <nav class="nav"><a style="left:95px">Home</a><a style="left:114.5px">About</a><a style="left:134.5px">Treatments</a><a style="left:164.7px">Services</a><a style="left:189px">Contact us</a></nav>
    <span class="book">Book Online</span>
  </header>
  <div class="hero hero--leaf" role="img" aria-label="Photo of a woman's eye peeking through large green leaves">
    <div class="hero-copy"><p class="hero-intro">WE ARE A WEIGHT LOSS CLINIC WITH<br>TOP EXPERTS AND PROFESSIONALS<br>PROVIDING DEDICATED SERVICES FOR</p><p class="hero-title">WEIGHT LOSS | WELLNESS | REJUVENATION</p></div>
  </div>
</section>
<p class="caption" style="left:28px"><strong>HOMEPAGE</strong> <small>- HEADER, MENU AND MAIN IMAGE</small></p>

<section class="screen screen--about">
  <div class="topbar"><span class="call">Call: 000 000 0000</span><span class="email">Email: contact@brightfernrx.com</span><span class="address">Address: Brightfern RX Headquarters Address information details t be added</span></div>
  <header class="site-header">
    <div class="brand"><span class="brand-dot"></span>Brightfernrx</div>
    <nav class="nav"><a style="left:82px">Home</a><a style="left:105px">About</a><a style="left:128px">Treatments</a><a style="left:161px">Services</a><a style="left:190px">Contact us</a></nav>
    <span class="book">Book Online</span>
  </header>
  <div class="hero hero--field" role="img" aria-label="Photo of a woman in a white shirt walking through a green field">
    <div class="hero-copy"><p class="hero-intro">WE ARE A WEIGHT LOSS CLINIC WITH<br>TOP EXPERTS AND PROFESSIONALS<br>PROVIDING DEDICATED SERVICES FOR</p><p class="hero-title">WEIGHT LOSS | WELLNESS | REJUVENATION</p></div>
  </div>
</section>
<p class="caption" style="left:318px"><strong>ABOUT</strong> <small>- HEADER, MENU AND MAIN IMAGE</small></p>

<section class="screen screen--treatments">
  <div class="topbar"><span class="call">Call: 000 000 0000</span><span class="email">Email: contact@brightfernrx.com</span><span class="address">Address: Brightfern RX Headquarters Address information details t be added</span></div>
  <header class="site-header">
    <div class="brand"><span class="brand-dot"></span>Brightfernrx</div>
    <nav class="nav"><a style="left:82px">Home</a><a style="left:105px">About</a><a style="left:128px">Treatments</a><a style="left:161px">Services</a><a style="left:190px">Contact us</a></nav>
    <span class="book">Book Online</span>
  </header>
  <div class="hero hero--foliage" role="img" aria-label="Photo of a woman among soft green foliage with a leaf across her face">
    <div class="hero-copy"><p class="hero-intro">WE ARE A WEIGHT LOSS CLINIC WITH<br>TOP EXPERTS AND PROFESSIONALS<br>PROVIDING DEDICATED SERVICES FOR</p><p class="hero-title">WEIGHT LOSS | WELLNESS | REJUVENATION</p></div>
  </div>
</section>
<p class="caption" style="left:608px"><strong>TREATMENTS</strong> <small>- HEADER, MENU AND MAIN IMAGE</small></p>

<section class="screen screen--services">
  <div class="topbar"><span class="call">Call: 000 000 0000</span><span class="email">Email: contact@brightfernrx.com</span><span class="address">Address: Brightfern RX Headquarters Address information details t be added</span></div>
  <header class="site-header">
    <div class="brand"><span class="brand-dot"></span>Brightfernrx</div>
    <nav class="nav"><a style="left:82px">Home</a><a style="left:105px">About</a><a style="left:128px">Treatments</a><a style="left:161px">Services</a><a style="left:190px">Contact us</a></nav>
    <span class="book">Book Online</span>
  </header>
  <div class="hero hero--mist" role="img" aria-label="Photo of a woman in profile against a misty blue-grey sky">
    <div class="hero-copy"><p class="hero-intro">WE ARE A WEIGHT LOSS CLINIC WITH<br>TOP EXPERTS AND PROFESSIONALS<br>PROVIDING DEDICATED SERVICES FOR</p><p class="hero-title">WEIGHT LOSS | WELLNESS | REJUVENATION</p></div>
  </div>
</section>
<p class="caption" style="left:898px"><strong>SERVICES</strong> <small>- HEADER, MENU AND MAIN IMAGE</small></p>

<h2 class="palette-title">COLOR SCHEME</h2>
<ul class="swatches">
  <li style="background:var(--deep-teal)"></li>
  <li style="background:var(--teal)"></li>
  <li style="background:var(--fern)"></li>
  <li style="background:var(--sky)"></li>
  <li style="background:var(--ocean)"></li>
  <li style="background:var(--mist)"></li>
  <li style="background:var(--ink)"></li>
</ul>

<aside class="draft-note">
  <p class="label">DRAFT 1: <small>First version for proof of concept for the 1st round of feedback</small></p>
  <p>Hello. Sorry for not having found your project earlier. I am very interested in developing a design that could be an option for your website.<br>
  To get us started I'm sending the preliminary version showing the color scheme and the atmosphere. My goal was a balance of visuals that would show professionalism but also<br>
  that would inspire women to see how it would feel to Brightfern. To inspire women to want the serenity that comes from your services.<br>
  I am currently developing the full pages, and I will send you the full set in the next couple of hours or so. If you would like to send me some feedback I can already start to integrate your feedback to the design.<br>
  Thank you</p>
</aside>

</body>
</html>
```